Amber Moth Glen- Luxury Tree-house Wellness Resort Website

Amber Moth Glen is a luxury nature wellness resort. Please look at our current website for content information and aesthetic. Brand
ing, imaging and color pallet all stay the same. We need the website simplified and easier to understand and better flow visually. More use of videos. I can send additional photos or videos. I love whimsical and magical. We don’t need to add extra content.
We have a vintage storybook theme with rich woods, alligator leather, nautical compasses, ship wheel, we have skeleton keys to miniature doors. Think Tobias under the hill. The concept is for the guest to stay and enjoy their time. Not travel to see other things. No fishing, no excursions. All on site, animals, gardens, games, meditation tools, relaxing and recharging. Again, please keep the same text and pictures that’s on the website now. I like adding as many slow videos as possible

Target Market(s)

Luxury Travelers. Wealthy Tourists.

Industry/Entity Type

Luxury Nature and Wellness Resort

Coding

Coded - Design and coding required

Number of Pages Required

4 page

Font styles to use
Serif
Script

Requirements
Must have
• All the photos and descriptions that are currently on the website. videos in the background. motion, textures
Nice to have
• Please ADD More pictures of the people/experience. I would like to have a textured background and maybe a palm leaf that is stationary in the lower right corner of the website that stays still while you scroll.

```html
<!DOCTYPE html>
<html lang="en">
<head>
<meta charset="utf-8">
<title>Amber Moth Glen — Luxury Boutique Resort</title>
<link href="https://fonts.googleapis.com/css2?family=Italiana&family=Montserrat:wght@400;500;600&family=Mrs+Saint+Delafield&display=swap" rel="stylesheet">
<style>
:root{
  --gold:#8d5a12;
  --gold-light:#c99a3f;
  --amber:#f0b54a;
  --ink:#1b1a18;
  --text:#2a2722;
  --cream:#f6f4de;
  --dark:#1d1c1a;
  --dark-card:#262523;
  --white:#ffffff;
  --line:#c9c3b5;
}
*{margin:0;padding:0;box-sizing:border-box}
html,body{width:1200px;height:4983px;overflow:hidden;background:var(--white)}
body{position:relative;font-family:'Montserrat',sans-serif;color:var(--text)}
.abs{position:absolute}
.serif{font-family:'Italiana',serif;font-weight:400}
.script{font-family:'Mrs Saint Delafield',cursive;font-weight:400}
.btn{position:absolute;display:flex;align-items:center;justify-content:center;background:var(--ink);color:var(--white);font-size:10px;font-weight:600;border-radius:4px;box-shadow:0 0 0 2px var(--white),0 0 0 3px var(--ink)}
.btn.light{background:transparent;border:1.5px solid var(--white);box-shadow:none;border-radius:3px}
.photo{position:absolute}
.ticks{position:absolute;list-style:none}
.ticks li{position:relative;padding-left:16px;text-transform:uppercase;font-size:11px;font-weight:500;letter-spacing:.2px;color:var(--ink);white-space:nowrap}
.ticks li::before{content:"";position:absolute;left:0;top:3px;width:9px;height:7px;background:var(--ink);clip-path:polygon(0 0,100% 50%,0 100%,30% 50%)}
.hero{left:110px;top:0;width:980px;height:455px;background:radial-gradient(ellipse at 55% 45%,#b8741f 0%,#6a3f14 35%,#2a1a0c 70%,#120c07 100%)}
.nav{left:110px;top:28px;width:980px;height:20px;font-size:10px;font-weight:500;color:var(--white)}
.nav a{position:absolute;color:var(--white);text-decoration:none;top:0;white-space:nowrap}
.nav a.active{color:var(--amber)}
.brand-mark{position:absolute;left:450px;top:-16px;width:80px;text-align:center;color:var(--gold-light);font-size:7px;letter-spacing:1px;line-height:1.2}
.brand-mark i{display:block;width:16px;height:16px;border:1px solid var(--gold-light);border-radius:50%;margin:0 auto 3px}
.hero-title{left:110px;width:980px;top:165px;text-align:center;font-size:76px;color:var(--white);line-height:1}
.hero-sub{left:110px;width:980px;top:245px;text-align:center;font-size:16px;font-weight:500;color:var(--white);line-height:1.35}
.h-center{left:110px;width:980px;text-align:center}
.h-big{font-size:36px;color:var(--ink)}
.body-s{font-size:10px;line-height:1.45;color:var(--ink)}
.band{left:110px;width:980px;background:var(--cream)}
.dark{left:110px;width:980px;background:radial-gradient(circle at 30% 40%,#252422,#181716 70%)}
.pkg{position:absolute;top:2684px;width:232px;height:358px;background:var(--dark-card)}
.pkg .img{height:155px}
.pkg h4{font-family:'Italiana',serif;font-weight:400;color:var(--white);font-size:19px;margin:17px 0 0 15px}
.pkg small{display:block;color:#8a867d;font-size:8px;margin:4px 0 0 15px}
.pkg hr{border:0;border-top:1px solid #6c6860;margin:9px 15px 0}
.pkg .ticks{position:static;margin:14px 0 0 15px}
.pkg .ticks li{color:var(--white);text-transform:none;font-size:9.5px;font-weight:400;height:21px}
.pkg .ticks li::before{background:var(--white)}
.field{position:absolute;border-bottom:1px solid var(--gold-light);color:#bdb7aa;font-size:9px;height:16px}
.footer{left:110px;top:4683px;width:980px;height:300px;background:var(--dark)}
.f-links{list-style:none;font-size:9px;color:var(--white)}
.f-links li{position:relative;padding-left:18px;height:19.3px;white-space:nowrap}
.f-links li::before{content:"";position:absolute;left:0;top:2px;width:8px;height:7px;background:var(--white);clip-path:polygon(0 0,100% 50%,0 100%,30% 50%)}
.social{position:absolute;width:12px;height:12px;border:1.5px solid var(--white);border-radius:50%;top:4942px}
</style>
</head>
<body>

<div class="abs hero" role="img" aria-label="Treehouse lodge with warm lantern-lit wooden decks at dusk"></div>
<svg class="abs" style="left:110px;top:360px" width="980" height="100" viewBox="0 0 980 100" aria-hidden="true">
  <path d="M0,60 C180,110 360,20 560,30 C760,40 850,90 980,70 L980,100 L0,100Z" fill="#fff"/>
</svg>
<nav class="abs nav">
  <a class="active" style="left:124px">Home</a>
  <a style="left:176px">Lodging</a>
  <a style="left:240px">Reunions &amp; Retreats</a>
  <a style="left:362px">Culinary</a>
  <div class="brand-mark"><i></i>AMBER MOTH GLEN</div>
  <a style="left:588px">Nature Immersion &amp; Homestead</a>
  <a style="left:763px">Discover</a>
  <a style="left:832px">nook</a>
</nav>
<h1 class="abs hero-title script">Amber Moth Glen</h1>
<p class="abs hero-sub">Luxury Boutique Resort &amp; Nature-Immersive Retreat<br>Located along the Saltmeadow coast, between Marsh Hollow &amp; Lantern Bay.</p>
<div class="btn" style="left:550px;top:312px;width:100px;height:24px">Read More</div>

<div class="abs" role="img" aria-label="Stationary palm frond decoration" style="left:110px;top:330px;width:110px;height:350px;background:linear-gradient(160deg,rgba(58,92,52,.55),rgba(58,92,52,0));border-radius:0 80px 0 0"></div>

<h2 class="abs h-center serif" style="top:508px;font-size:32px;color:var(--gold)">About Us</h2>
<p class="abs h-center" style="top:550px;font-size:10px;color:var(--ink)">Designed for privacy, elevated accommodations, and meaningful connection.</p>
<h3 class="abs serif" style="left:232px;top:614px;font-size:36px;color:var(--ink)">Amber Moth Glen Intro</h3>
<div class="abs body-s" style="left:232px;top:674px;width:400px">
  <p>The resort offers a refined outdoor escape that blends comfort, intention, and experiential luxury. Elevated Treehouse-Style accommodations, a private lodge, pools, hot tub, and immersive homestead and gardening experiences.</p>
  <p style="margin-top:10px">Personalized with curated surprises tailored to the group.</p>
  <p style="margin-top:10px">Guests are invited to slow down and reconnect through nature immersion, in-unit spa and meditation tools, wildlife-viewing supplies, campfires, and hands-on outdoor activities—all within a peaceful, secluded environment designed for presence and restoration. Ideal for family reunions, couples, solo travelers, creatives, wellness seekers, elopements, birthdays, and small private retreats.</p>
  <p style="margin-top:10px">Disconnect to Connect.</p>
</div>
<div class="btn" style="left:234px;top:861px;width:102px;height:25px">Read More</div>
<div class="photo" role="img" aria-label="Squirrel perched on a weathered stump" style="left:668px;top:642px;width:127px;height:132px;background:linear-gradient(150deg,#b7b3a6,#6f6a5c)"></div>
<div class="photo" role="img" aria-label="Mossy tree trunk in a green forest" style="left:805px;top:610px;width:161px;height:164px;background:linear-gradient(160deg,#5f7a3b,#2f3f22)"></div>
<div class="photo" role="img" aria-label="Vintage brass compass detail" style="left:710px;top:782px;width:85px;height:91px;background:linear-gradient(150deg,#8b6a3a,#3b2a16)"></div>
<div class="photo" role="img" aria-label="Warm wooden interior with string lights" style="left:805px;top:782px;width:118px;height:122px;background:linear-gradient(150deg,#c27a34,#5a2f12)"></div>

<div class="abs band" style="top:1000px;height:273px"></div>
<div class="photo" role="img" aria-label="Moss-draped live oak with sunlight through the branches" style="left:232px;top:954px;width:329px;height:371px;background:linear-gradient(170deg,#c9b86a,#5a5a2c 45%,#23260f)"></div>
<h2 class="abs serif" style="left:620px;top:1040px;font-size:37px;line-height:40px;color:var(--ink);white-space:nowrap">Immerse Yourself In Coastal<br>Culture &amp; Wildlife</h2>
<p class="abs serif" style="left:620px;top:1125px;font-size:29px;color:var(--gold-light);white-space:nowrap">Limited Seasonal Availability</p>
<p class="abs" style="left:620px;top:1169px;font-size:9px;color:var(--ink)">Curated Guest Experiences Privacy By Design</p>
<div class="btn" style="left:622px;top:1203px;width:101px;height:25px">Read More</div>

<p class="abs h-center" style="top:1370px;font-size:29px;color:var(--gold)">Accommodations</p>
<h2 class="abs h-center serif h-big" style="top:1408px">Custom curated Adventures</h2>
<div class="abs" style="left:211px;top:1538px;width:778px;height:457px;border:2px solid #d9d6cf;border-radius:12px"></div>
<div class="photo" role="img" aria-label="Main house with wraparound porches" style="left:232px;top:1486px;width:345px;height:79px;background:linear-gradient(180deg,#6f8db0,#8c8a7a 60%,#4a4a3e);border-radius:4px"></div>
<div class="photo" role="img" aria-label="Luxury tent cabin in black and white" style="left:623px;top:1486px;width:343px;height:79px;background:linear-gradient(180deg,#b8b8b8,#555 60%,#222);border-radius:4px"></div>
<p class="abs serif" style="left:232px;width:345px;top:1576px;text-align:center;font-size:17px;color:var(--ink)">Main Housh</p>
<p class="abs serif" style="left:623px;width:343px;top:1576px;text-align:center;font-size:17px;color:var(--ink)">LUXURY TENTS</p>
<h3 class="abs serif" style="left:255px;top:1645px;font-size:31px;color:var(--ink)">Bramblewick</h3>
<div class="abs" style="left:255px;top:1693px;width:300px;border-top:1px solid #555"></div>
<ul class="ticks" style="left:255px;top:1706px;line-height:19.6px">
  <li>Hosts 17 guests</li><li>Hot tub</li><li>Campfire, BBQ &amp; S'mores</li><li>Chef's kitchen</li><li>Hidden treasure rooms</li><li>Mini golf, swings</li><li>Sleeping porch</li><li>Games &amp; music nights</li><li>5 bedrooms &amp; 5 bunk beds</li><li>Sleeps 9 adults &amp; 8 children</li><li>3.5 bathrooms</li><li>Curated surprises</li>
</ul>
<div class="photo" role="img" aria-label="Wood-paneled lodge living room with stone fireplace" style="left:598px;top:1623px;width:368px;height:351px;background:linear-gradient(160deg,#c07a3a,#8a4a20 50%,#4b2a14);border-radius:8px"></div>
<svg class="abs" style="left:922px;top:1938px" width="24" height="16" viewBox="0 0 24 16" aria-hidden="true"><path d="M2 8h19M15 2l6 6-6 6" fill="none" stroke="#fff" stroke-width="1.6"/></svg>

<div class="abs band" style="top:2070px;height:405px"></div>
<div class="photo" role="img" aria-label="Bare tree against a purple sunset over marshland" style="left:232px;top:2121px;width:171px;height:288px;background:linear-gradient(180deg,#8d7fb0,#c79aa0 45%,#5c5a38);border-radius:6px"></div>
<div class="photo" role="img" aria-label="Raised cottage among live oaks and pond" style="left:416px;top:2121px;width:170px;height:288px;background:linear-gradient(180deg,#b6c2c4,#55613a 55%,#2b3320);border-radius:6px"></div>
<div class="abs" style="left:350px;top:2210px;width:116px;height:116px;border-radius:50%;background:var(--amber);opacity:.93;display:flex;flex-direction:column;align-items:center;justify-content:center;color:var(--white);text-align:center">
  <span class="serif" style="font-size:24px;line-height:1">Luxury</span>
  <span class="serif" style="font-size:15px">Experiences</span>
</div>
<h2 class="abs serif" style="left:646px;top:2152px;font-size:37px;color:var(--ink);white-space:nowrap">Reunions &amp; Retreats</h2>
<ul class="ticks" style="left:648px;top:2206px;line-height:19.7px">
  <li>Family reunions</li><li>Birthday parties</li><li>Solo travelers</li><li>Treasure hunts</li><li>Bird watching</li><li>Homestead experience</li><li>Farm animals</li><li>Campfires &amp; S'mores</li><li>Private &amp; exclusive</li>
</ul>

<div class="abs dark" style="top:2475px;height:695px"></div>
<p class="abs" style="left:232px;top:2532px;font-size:29px;color:var(--gold-light)">Packages</p>
<h2 class="abs serif" style="left:232px;top:2570px;font-size:38px;line-height:41px;color:var(--white);white-space:nowrap">Custom Curated Adventures &amp;<br>Packages For Each Guest</h2>
<div class="pkg" style="left:232px">
  <div class="img" role="img" aria-label="Platter of fresh local seafood" style="background:linear-gradient(150deg,#c8cdd0,#c2583a 55%,#6d3a24)"></div>
  <h4>CULINARY</h4><small>A Taste Of Local</small><hr>
  <ul class="ticks"><li>Private Chef Option</li><li>Fresh Local Seafood</li><li>S'mores &amp; Snacks</li><li>BBQ Grilling</li><li>Pre-Stocked Fridge &amp; Cooler</li><li>Farm to Table</li></ul>
</div>
<div class="pkg" style="left:484px">
  <div class="img" role="img" aria-label="Bird perched on a branch in the woods" style="background:linear-gradient(150deg,#6d8a4a,#3e5a2a 60%,#22301a)"></div>
  <h4>ADVENTURE</h4><small>Discover The Magic</small><hr>
  <ul class="ticks"><li>Wildlife Viewing</li><li>Homestead Adventure</li><li>Campfire Building</li><li>Treasure &amp; Games</li><li>Arts and Crafts</li><li>Find Lost Time</li></ul>
</div>
<div class="pkg" style="left:735px">
  <div class="img" role="img" aria-label="Guest relaxing during a spa and yoga session" style="background:linear-gradient(150deg,#e6d3c0,#c89a78 55%,#8a5a3e)"></div>
  <h4>RELAXATION</h4><small>Recharge Your Soul</small><hr>
  <ul class="ticks"><li>Nature Immersion</li><li>Meditation Tools</li><li>Bird Watching</li><li>Aroma Therapy</li><li>Earthing/Grounding</li><li>Top Deck Yoga</li></ul>
</div>
<div class="btn light" style="left:536px;top:3082px;width:128px;height:30px">See All Packages</div>

<p class="abs h-center" style="top:3218px;font-size:29px;color:var(--gold)">Our Gallery</p>
<h2 class="abs h-center serif h-big" style="top:3254px">Nature Immersion &amp; Homestead</h2>
<div class="photo" role="img" aria-label="Treehouse with fire pit glowing at night" style="left:232px;top:3367px;width:234px;height:234px;background:linear-gradient(170deg,#2a3f6a,#c07028 60%,#3a2210)"></div>
<div class="photo" role="img" aria-label="Raised wooden lodge lit with string lights" style="left:478px;top:3328px;width:244px;height:314px;background:linear-gradient(175deg,#4a3a2a,#d49a4a 55%,#5a3616)"></div>
<div class="photo" role="img" aria-label="Live oaks framing a marsh at sunset" style="left:731px;top:3367px;width:235px;height:234px;background:linear-gradient(170deg,#6e7a80,#4a5030 55%,#c8a46a)"></div>
<svg class="abs" style="left:206px;top:3476px" width="40" height="22" viewBox="0 0 40 22" aria-hidden="true"><circle cx="22" cy="11" r="10" fill="none" stroke="#555" stroke-width="1"/><path d="M38 11H4M10 5L4 11l6 6" fill="none" stroke="#555" stroke-width="1.2"/></svg>
<svg class="abs" style="left:954px;top:3476px" width="40" height="22" viewBox="0 0 40 22" aria-hidden="true"><circle cx="18" cy="11" r="10" fill="none" stroke="#555" stroke-width="1"/><path d="M2 11h34M30 5l6 6-6 6" fill="none" stroke="#555" stroke-width="1.2"/></svg>

<div class="abs" role="img" aria-label="Slow background video of live oaks over the marsh" style="left:110px;top:3705px;width:980px;height:416px;background:linear-gradient(180deg,#6b7468,#4e5a44 45%,#2f3a26)"></div>
<div class="abs" style="left:578px;top:3881px;width:64px;height:64px;border:1.5px solid var(--white);border-radius:50%;display:flex;align-items:center;justify-content:center;color:var(--white);font-size:12px">PLAY</div>

<div class="abs dark" style="top:4121px;height:562px"></div>
<div class="photo" role="img" aria-label="Resort concierge at the front desk" style="left:110px;top:4199px;width:451px;height:484px;background:linear-gradient(180deg,#a8722e,#3a3030 55%,#d8d8d8)"></div>
<p class="abs" style="left:600px;top:4272px;font-size:29px;color:var(--gold-light)">Contact Us</p>
<h2 class="abs serif" style="left:600px;top:4316px;font-size:38px;color:var(--white);white-space:nowrap">Discover the magic</h2>
<div class="field" style="left:600px;top:4392px;width:168px">Name</div>
<div class="field" style="left:797px;top:4392px;width:169px">Last Name</div>
<div class="field" style="left:600px;top:4450px;width:168px">Email</div>
<div class="field" style="left:797px;top:4450px;width:169px">Phone</div>
<div class="field" style="left:600px;top:4508px;width:366px">Message</div>
<div class="btn light" style="left:600px;top:4561px;width:102px;height:31px;font-weight:500;font-size:9px">Submit</div>

<footer class="abs footer"></footer>
<div class="abs" style="left:270px;top:4752px;width:80px;height:80px;border:1.5px solid var(--gold-light);border-radius:50%"></div>
<p class="abs serif" style="left:200px;width:220px;top:4838px;text-align:center;font-size:20px;letter-spacing:1px;color:var(--gold-light)">Amber Moth Glen</p>
<p class="abs" style="left:232px;top:4874px;width:190px;font-size:8.5px;line-height:1.35;color:var(--white)">Lorem ipsum dolor sit amet, consectetur adipiscing elit, sed do eiusmod tempor incididunt ut labore et dolore magna aliqua.</p>
<h3 class="abs serif" style="left:519px;top:4745px;font-size:25px;color:var(--white)">Quick Links</h3>
<ul class="abs f-links" style="left:519px;top:4790px">
  <li>Home</li><li>Lodging</li><li>Reunions &amp; Retreats</li><li>Culinary</li><li>Nature Immersion &amp; Homestead</li><li>Discover</li><li>nook</li>
</ul>
<h3 class="abs serif" style="left:770px;top:4745px;font-size:25px;color:var(--white)">Contact Us</h3>
<svg class="abs" style="left:770px;top:4790px" width="18" height="18" viewBox="0 0 18 18" aria-hidden="true"><circle cx="9" cy="9" r="8" fill="none" stroke="#c99a3f" stroke-width="1.3"/><path d="M6 5l2 2-1 1.2c.6 1.2 1.6 2.2 2.8 2.8L11 10l2 2-1.2 1.2C8.5 13 5 9.5 4.8 6.2Z" fill="#c99a3f"/></svg>
<p class="abs" style="left:797px;top:4795px;font-size:9px;color:var(--white)">555-014-2290</p>
<svg class="abs" style="left:770px;top:4826px" width="18" height="18" viewBox="0 0 18 18" aria-hidden="true"><circle cx="9" cy="9" r="8" fill="none" stroke="#c99a3f" stroke-width="1.3"/><rect x="4.5" y="6" width="9" height="6.5" fill="none" stroke="#c99a3f" stroke-width="1.1"/><path d="M4.5 6l4.5 3.5L13.5 6" fill="none" stroke="#c99a3f" stroke-width="1.1"/></svg>
<p class="abs" style="left:797px;top:4831px;font-size:9px;color:var(--white)">hello@ambermothglen.com</p>
<svg class="abs" style="left:770px;top:4862px" width="18" height="18" viewBox="0 0 18 18" aria-hidden="true"><circle cx="9" cy="9" r="8" fill="none" stroke="#c99a3f" stroke-width="1.3"/><path d="M9 14s-3.5-3.6-3.5-6a3.5 3.5 0 017 0c0 2.4-3.5 6-3.5 6z" fill="#c99a3f"/><circle cx="9" cy="8" r="1.2" fill="#1d1c1a"/></svg>
<p class="abs" style="left:797px;top:4866px;width:170px;font-size:9px;line-height:1.35;color:var(--white)">27 Lantern Fern Road, Marsh Hollow 30000</p>
<p class="abs" style="left:232px;top:4944px;font-size:8px;color:#9a958a">Copyright © 2026 Amber Moth Glen. All rights reserved</p>
<span class="social" style="left:850px"></span>
<span class="social" style="left:879px"></span>
<span class="social" style="left:908px"></span>
<span class="social" style="left:937px"></span>

</body>
</html>
```